Business Card for Flight Instructor/Commercial Pilot

I need a business card for myself as a Flight Instructor. I'm a certificated flight instructor at a local flight school in St Paul, MN and want to have a business card that I can give out both to prospective students and also to prospective employers in commercial/business aviation. The business card should have a few elements to it (my name, my position, and my ZRT certifications:
Dorian Welkes, MBA
Flight Instructor
CFI, CFII, AGI, IGI
Then lastly, I'd like it to include my phone number for calls or texts, my email address, and my Corvanet url. I'll provide all of these at a later point.

If we can include some kind of aviation graphic, that's great, but I don't currently have a logo and I don't necessarily need one, so don't feel like a logo is required here, it's not. I'm but I'm open to whatever you might put together. But I honestly don't need a logo, just good design with a simple graphic element to draw a little interest.
I'd also like to add a short tag line. A few ideas I have are:
- Fly Smart. Stay Humble. Never Stop Learning.
- Train smart. Fly safe. Have fun.
- Master the craft. Enjoy the flight.

For the back side, I'm open to ideas on what to put there. maybe the tagline could go there, or a QR code for my Corvanet page, or maybe something else.

Target audience is both prospective students who are interested in learning to fly (or adding more ratings) and commercial aviation companies that could be potential employer for me in commercial aviation. Trying to portray a sense of professionalism, trust, and high level of competency.

The business card doesn’t have to be standard (rectangular with square corners) and I’m open to suggestions for based on the design.
Lastly, I just don't want the design created by AI.
Let me know if you need any further info. Thanks!

```html
<!DOCTYPE html>
<html lang="en">
<head>
<meta charset="utf-8">
<title>Dorian Welkes – Flight Instructor Business Card</title>
<link href="https://fonts.googleapis.com/css2?family=Poppins:wght@400;500;600;700&display=swap" rel="stylesheet">
<style>
  :root {
    --page-bg: #e6e2dd;
    --card-light: #f4f6f8;
    --card-mid: #dde3e8;
    --teal: #1d5169;
    --teal-deep: #143a4f;
    --band-dark: #1f2325;
    --ink-teal: #1a4559;
    --ink-grey: #33393d;
    --contact-text: #f3ecec;
    --icon-fill: #e9dfdc;
  }
  * { margin: 0; padding: 0; box-sizing: border-box; }
  html, body {
    width: 1200px;
    height: 970px;
    overflow: hidden;
    background: var(--page-bg);
    font-family: "Poppins", sans-serif;
  }
  .canvas {
    position: relative;
    width: 1200px;
    height: 970px;
  }
  .business-card {
    position: absolute;
    left: 60px;
    top: 176px;
    width: 1080px;
    height: 617px;
    border-radius: 26px;
    overflow: hidden;
    background: linear-gradient(160deg, var(--card-light) 0%, var(--card-mid) 100%);
    box-shadow: 0 18px 40px rgba(0, 0, 0, 0.18);
  }
  .card-waves {
    position: absolute;
    inset: 0;
    width: 100%;
    height: 100%;
  }
  .identity {
    position: absolute;
    left: 55px;
    top: 64px;
  }
  .identity-name {
    font-size: 35px;
    font-weight: 600;
    color: var(--ink-teal);
    line-height: 1.1;
  }
  .identity-role,
  .identity-certs {
    font-size: 24px;
    font-weight: 400;
    color: var(--ink-grey);
    line-height: 1.55;
  }
  .identity-role { margin-top: 4px; }
  .brand-name {
    position: absolute;
    left: 560px;
    top: 226px;
    font-size: 50px;
    font-weight: 600;
    color: var(--ink-teal);
    line-height: 1;
    letter-spacing: 0.5px;
  }
  .contact-list {
    position: absolute;
    left: 55px;
    top: 442px;
    list-style: none;
  }
  .contact-item {
    display: flex;
    align-items: center;
    gap: 12px;
    height: 39px;
    font-size: 27px;
    font-weight: 400;
    color: var(--contact-text);
    letter-spacing: 0.3px;
  }
  .contact-icon {
    width: 30px;
    height: 30px;
    flex: none;
  }
</style>
</head>
<body>
<main class="canvas">
  <section class="business-card">
    <svg class="card-waves" viewBox="0 0 1180 674" preserveAspectRatio="none" aria-hidden="true">
      <defs>
        <linearGradient id="tealFill" x1="0" y1="0" x2="1" y2="1">
          <stop offset="0" stop-color="#245d78"/>
          <stop offset="1" stop-color="#143a4f"/>
        </linearGradient>
      </defs>
      <path class="wave-teal" fill="url(#tealFill)"
        d="M0,380 C250,345 500,392 720,442 C860,472 1010,474 1180,470 L1180,674 L0,674 Z"/>
      <path class="wave-crest" fill="var(--teal)"
        d="M640,395 C800,392 1000,340 1180,258 L1180,332 C1050,392 900,412 640,395 Z"/>
      <path class="wave-band" fill="var(--band-dark)"
        d="M0,285 C220,265 450,320 640,380 C820,440 1000,432 1180,405 L1180,487 C980,497 800,472 650,432 C450,382 250,350 0,365 Z"/>
    </svg>

    <div class="identity">
      <h1 class="identity-name">Dorian Welkes, MBA</h1>
      <p class="identity-role">Flight Instructor</p>
      <p class="identity-certs">CFI, CFII, AGI, IGI</p>
    </div>

    <p class="brand-name">Dorian Welkes</p>

    <ul class="contact-list">
      <li class="contact-item">
        <svg class="contact-icon" viewBox="0 0 30 30" aria-hidden="true">
          <circle cx="15" cy="15" r="15" fill="var(--icon-fill)"/>
          <path d="M8,12 C8,9 22,9 22,12 L20,13.5 L18,12 L12,12 L10,13.5 Z M10,15 L20,15 L21,21 L9,21 Z" fill="var(--teal-deep)"/>
        </svg>
        <span>(555) 418-7302</span>
      </li>
      <li class="contact-item">
        <svg class="contact-icon" viewBox="0 0 30 30" aria-hidden="true">
          <circle cx="15" cy="15" r="15" fill="var(--icon-fill)"/>
          <rect x="8" y="10" width="14" height="10" rx="1" fill="var(--teal-deep)"/>
          <path d="M8.5,10.5 L15,15.5 L21.5,10.5" fill="none" stroke="var(--icon-fill)" stroke-width="1.3"/>
        </svg>
        <span>company@skymail.com</span>
      </li>
      <li class="contact-item">
        <svg class="contact-icon" viewBox="0 0 30 30" aria-hidden="true">
          <circle cx="15" cy="15" r="15" fill="var(--icon-fill)"/>
        </svg>
        <span>Corvanet url.com</span>
      </li>
    </ul>
  </section>
</main>
</body>
</html>
```